Custom Bladeless LASIK Poster Design Project

I would like a poster whose theme will also be used for future brochures. I would also like it to be created in such a way that it can be part of an in-office branding campaign. Our company already has a logo. We are the premier Ophthalmology group in Orange County, NY specializing in Cataract and Laser Refractive surgery. This particular poster should highlight the advantages to Custom Bladeless LASIK and mention our free consultations and website www.brightmorrowsight.com
Updates

Would like to make sure the color palette complements the colors in our logo.   Also try incorporating the phrase "Regain your Sight, Regain your Life"

The message should also invite the patient to inquire about more information or to tell a friend about our services

just uploaded the full zip file, please try again.

I just uploaded the full zip file for our logo.  Please let me know if there is still a problem.  Thanks

poster size should be 24" wide 32" high

and able to reduce it to 18"W x 24"H

Thank you 
The designer I choose will also be used in near future for other poster and in office materials highlighting our other services

Reason: I would like to give the other designers that accepted our invitation an opportunity to submit a design.

Industry/Entity Type

It Company

Requirements
Must have
• attractive young and active male or female model extolling the virtues of eliminating there glasses and contact lenses.

```html
<!DOCTYPE html>
<html lang="en">
<head>
<meta charset="utf-8">
<title>Custom Bladeless LASIK Poster</title>
<link rel="stylesheet" href="https://fonts.googleapis.com/css2?family=Crimson+Pro:wght@400;600;700&display=swap">
<style>
  :root {
    --page: #ffffff;
    --wine: #5b0e10;
    --crimson: #8e1b1c;
    --navy: #1f2746;
    --panel: rgba(236, 208, 208, 0.55);
    --body-text: #7a1a1a;
  }
  * { box-sizing: border-box; margin: 0; padding: 0; }
  html, body {
    width: 1200px; height: 900px; overflow: hidden;
    background: var(--page);
    font-family: "Crimson Pro", "Palatino Linotype", Georgia, serif;
  }
  .poster {
    position: absolute; left: 301px; top: 12px;
    width: 620px; height: 877px; overflow: hidden;
    background: var(--wine);
  }
  .poster__photo {
    position: absolute; left: 0; top: 0; width: 100%; height: 100%;
    background:
      linear-gradient(180deg, #5b0e10 0, #5b0e10 122px, rgba(91,14,16,0) 123px),
      radial-gradient(ellipse 30% 22% at 28% 30%, #e6c1aa 0, rgba(230,193,170,0) 100%),
      radial-gradient(ellipse 60% 30% at 55% 72%, #d9a98c 0, rgba(217,169,140,0) 100%),
      linear-gradient(180deg, #d8cfc8 0%, #e9e3df 45%, #c9a48d 65%, #1d2540 88%, #2b2622 100%);
  }
  .poster__panel {
    position: absolute; left: 282px; top: 122px;
    width: 338px; height: 544px;
    background: var(--panel);
  }
  .poster__copy {
    position: absolute; right: 26px; top: 150px; width: 330px;
    text-align: right;
  }
  .title { color: var(--crimson); font-weight: 700; line-height: 1; }
  .title__main { display: block; font-size: 31px; }
  .title__sub { display: block; font-size: 25px; margin-top: 2px; }
  .headline {
    margin-top: 30px; color: var(--navy);
    font-size: 41px; font-weight: 700; line-height: 1.02;
  }
  .body-copy {
    margin: 40px 0 0 auto; width: 212px; text-align: center;
    color: var(--body-text); font-size: 12.5px; line-height: 1.18;
  }
  .cta {
    margin: 14px 0 0 auto; width: 226px; text-align: center;
    color: var(--crimson); font-size: 16px; font-weight: 700; line-height: 1.2;
  }
  .practice {
    margin: 22px 0 0 auto; width: 210px; text-align: center;
    color: var(--crimson);
  }
  .practice__mark {
    display: block; width: 16px; height: 16px; margin: 0 auto 8px;
    border-radius: 50%; background: var(--crimson);
  }
  .practice__name {
    font-size: 15px; font-weight: 700; letter-spacing: 0.08em; line-height: 1.15;
  }
  .practice__address {
    margin-top: 10px; font-size: 11px; font-weight: 700; line-height: 1.25;
  }
  .practice__web {
    margin-top: 10px; font-size: 15px; font-weight: 700;
  }
</style>
</head>
<body>
  <main class="poster">
    <div class="poster__photo" role="img" aria-label="Photograph of a smiling active adult riding an exercise bike in a fitness class, free of glasses, with other riders blurred behind"></div>
    <div class="poster__panel"></div>
    <section class="poster__copy">
      <h1 class="title">
        <span class="title__main">Custom Bladeless</span>
        <span class="title__sub">LASIK</span>
      </h1>
      <h2 class="headline">Regain your Sight,<br>Regain your Life.</h2>
      <p class="body-copy">It’s always nicer to enjoy fitness activities without eye glasses or contact lenses. Custom Bladeless LASIK promises you a new freedom and a better way of life.</p>
      <p class="cta">Ask about your free consultation, and tell a friend about us.</p>
      <div class="practice">
        <span class="practice__mark"></span>
        <p class="practice__name">BRIGHTMORROW<br>EYE SURGEONS</p>
        <p class="practice__address">48 Harbor Lane, Suite 310<br>Millbrook, NY 12545<br>845.555.0142</p>
        <p class="practice__web">www.brightmorrowsight.com</p>
      </div>
    </section>
  </main>
</body>
</html>
```